Brimovex business card

Based on company logo and website given , to design a business card temple. Slogan "Your furry friends deserves the best"
Color style please refer to our website

```html
<!DOCTYPE html>
<html lang="en">
<head>
<meta charset="utf-8">
<title>Brimovex business card</title>
<link href="https://fonts.googleapis.com/css2?family=Arimo:wght@400;700&family=Open+Sans:wght@400;600&display=swap" rel="stylesheet">
<style>
  :root {
    --forest: #06443f;
    --olive: #c3b52e;
    --lime: #d6cf3c;
    --lime-light: #e2de56;
    --white: #ffffff;
    --backdrop: #5a5a5a;
    --ink: #0d3f3a;
  }
  * { box-sizing: border-box; margin: 0; padding: 0; }
  html, body { width: 1200px; height: 1036px; overflow: hidden; }
  body {
    background: var(--backdrop);
    font-family: "Arimo", Arial, sans-serif;
    position: relative;
  }
  .card {
    position: absolute;
    left: 185px;
    width: 830px;
    height: 455px;
    overflow: hidden;
    box-shadow: 0 10px 30px rgba(0,0,0,.35);
  }
  .card--back { top: 40px; background: var(--forest); }
  .card--front { top: 541px; background: var(--white); }

  /* back */
  .back__media-panel {
    position: absolute; left: 0; top: 0; width: 390px; height: 100%;
    background: var(--lime);
  }
  .back__photo {
    position: absolute; left: 45px; top: 38px; width: 290px; height: 380px;
    background: linear-gradient(180deg, #efe9dc 0%, #e6e6e0 40%, #dcdfd6 100%);
  }
  .back__info {
    position: absolute; left: 390px; top: 0; right: 0; bottom: 0;
    color: var(--white); text-align: center;
  }
  .brand-name {
    font-family: "Arimo", Arial, sans-serif;
    font-weight: 700;
    color: var(--olive);
    letter-spacing: 1px;
  }
  .back__brand { font-size: 62px; margin-top: 62px; display: block; }
  .hours__title {
    font-size: 20px; letter-spacing: 1px; margin-top: 22px; font-weight: 400;
  }
  .hours__list {
    list-style: none; width: 300px; margin: 16px auto 0; font-size: 19px;
  }
  .hours__row { display: flex; align-items: baseline; line-height: 28px; }
  .hours__day { white-space: nowrap; }
  .hours__dots { flex: 1; border-bottom: 2px dotted rgba(255,255,255,.8); margin: 0 8px; transform: translateY(-5px); }
  .hours__time { white-space: nowrap; }
  .back__web { font-size: 30px; color: var(--olive); margin-top: 24px; }

  /* front */
  .front__art { position: absolute; inset: 0; }
  .front__pets {
    position: absolute; left: 28px; top: 100px; width: 280px; height: 115px;
    background: linear-gradient(90deg, #d7a679 0%, #6b6b6b 35%, #4b4e55 60%, #e6d4ad 100%);
    border-radius: 8px;
  }
  .front__brand {
    position: absolute; left: 330px; top: 92px; width: 430px; text-align: center;
    font-size: 76px;
  }
  .front__services {
    position: absolute; left: 330px; top: 200px; width: 430px;
    display: flex; justify-content: center; gap: 22px;
    font-family: "Open Sans", Arial, sans-serif; font-size: 17px; color: var(--white);
  }
  .contact {
    position: absolute; left: 55px; top: 300px; display: flex; gap: 10px;
  }
  .contact__rail {
    width: 30px; height: 136px; border-radius: 15px; background: var(--forest);
    display: flex; flex-direction: column; align-items: center; justify-content: space-around;
    padding: 8px 0;
  }
  .contact__rail svg { width: 16px; height: 16px; }
  .contact__lines {
    list-style: none; font-size: 17px; line-height: 22.5px; color: var(--ink); padding-top: 2px;
  }
</style>
</head>
<body>

<section class="card card--back" aria-label="Card back">
  <div class="back__media-panel">
    <div class="back__photo" role="img" aria-label="Photo of a cream labrador puppy lying on a street map of the shop location"></div>
  </div>
  <div class="back__info">
    <span class="brand-name back__brand">Brimovex</span>
    <h2 class="hours__title">WORKING HOURS</h2>
    <ul class="hours__list">
      <li class="hours__row"><span class="hours__day">Monday</span><span class="hours__dots"></span><span class="hours__time">9 am - 5 pm</span></li>
      <li class="hours__row"><span class="hours__day">Tuesday</span><span class="hours__dots"></span><span class="hours__time">9 am - 5 pm</span></li>
      <li class="hours__row"><span class="hours__day">Wednesday</span><span class="hours__dots"></span><span class="hours__time">9 am - 5 pm</span></li>
      <li class="hours__row"><span class="hours__day">Thursday</span><span class="hours__dots"></span><span class="hours__time">9 am - 5 pm</span></li>
      <li class="hours__row"><span class="hours__day">Friday</span><span class="hours__dots"></span><span class="hours__time">9 am - 5 pm</span></li>
      <li class="hours__row"><span class="hours__day">Saturday</span><span class="hours__dots"></span><span class="hours__time">close</span></li>
    </ul>
    <p class="back__web">www.brimovex.com.au</p>
  </div>
</section>

<section class="card card--front" aria-label="Card front">
  <svg class="front__art" viewBox="0 0 830 455" preserveAspectRatio="none" aria-hidden="true">
    <path d="M0 0 H830 V200 C760 270 660 300 560 285 C430 265 300 205 170 212 C100 216 40 235 0 262 Z" fill="var(--forest)"/>
    <path d="M0 300 C120 240 260 235 420 270 C560 300 700 320 830 270 V345 C700 385 570 360 440 320 C300 278 150 262 0 300 Z" fill="var(--olive)"/>
    <path d="M120 255 C260 232 400 262 520 292 C640 322 740 322 830 288 V318 C730 352 620 340 500 305 C380 272 250 250 120 255 Z" fill="var(--lime-light)"/>
    <path d="M380 265 C420 280 440 300 450 360 L452 395 C440 340 420 300 380 265 Z" fill="var(--olive)"/>
  </svg>
  <div class="front__pets" role="img" aria-label="Photo of two long-haired cats and two puppies lying in a row"></div>
  <span class="brand-name front__brand">Brimovex</span>
  <p class="front__services"><span>Pet Diets</span><span>Vet Medicine</span><span>Service</span></p>
  <div class="contact">
    <div class="contact__rail">
      <svg viewBox="0 0 16 16" aria-hidden="true"><path d="M8 1 L15 8 H13 V15 H3 V8 H1 Z" fill="var(--lime)"/></svg>
      <svg viewBox="0 0 16 16" aria-hidden="true"><path d="M3 1 L6 4 L4.5 6 C5.5 8.5 7.5 10.5 10 11.5 L12 10 L15 13 L13 15 C7 14 2 9 1 3 Z" fill="var(--lime)"/></svg>
      <svg viewBox="0 0 16 16" aria-hidden="true"><circle cx="8" cy="8" r="7" fill="none" stroke="var(--lime)" stroke-width="1.6"/><path d="M1 8 H15 M8 1 C4 5 4 11 8 15 M8 1 C12 5 12 11 8 15" fill="none" stroke="var(--lime)" stroke-width="1.2"/></svg>
      <svg viewBox="0 0 16 16" aria-hidden="true"><rect x="1" y="3" width="14" height="10" fill="var(--lime)"/><path d="M1 3 L8 9 L15 3" fill="none" stroke="var(--forest)" stroke-width="1.2"/></svg>
    </div>
    <ul class="contact__lines">
      <li>12/40 Harlow Street</li>
      <li>Glenmere Vic 3188</li>
      <li>+61 3 9000 4127</li>
      <li>1800 000 312</li>
      <li>www.brimovex.com.au</li>
      <li>sales@brimovex.com.au</li>
    </ul>
  </div>
</section>

</body>
</html>
```